Business card for acupunctist in Melbourne. Specialises in Fertility, pre and post natal care, pain

I am looking for a business card which is going to catch people eyes. Two sided, one side in a muted colour (keeping it feminine) (pink or yellow???)maybe with a little simple logo or picture, the other side I was thinking white with 3 colours (pink grey and yellow... Had these in mind.
Info on the card
Marla Quenby Acupuncture

Dr Marla Quenby (TCM Acupuncture)
Acupuncture for balancing body and mind.
Fernleaf Wellcraft
14 Corran Lane, Elsworth 3071.
94726150
0438219574
Marlatcm@quenbymail.com

Some other little logo/ designs I have liked are as follows:
http://www.dorisfelkaclinic.com/rates-and-insurance/
http://www.corinnetavish.com/
http://www.rz-needlework.co.uk/

Target Market(s)

professional women, people in pain, active people, people seeking a healthy lifefstyle.

Industry/Entity Type

Business

Font styles to use
Serif
Sans Serif

Colors
eea4c8
fde08a
aaaaaa

Requirements
Must have
• Must be eye catching, but not too loud and busy. Subltle is good. Simple is also good. The logo could be something that represents growth and health and nurturing. Again not too elaborate, very simple.
Thankyou
Should not have
• Electric colours, crazy fonts, Pictures of yin and yang, candles, or bodies.

```html
<!DOCTYPE html>
<html lang="en">
<head>
<meta charset="utf-8">
<title>Marla Quenby Acupuncture – Business Card</title>
<link rel="stylesheet" href="https://fonts.googleapis.com/css2?family=Questrial&display=swap">
<style>
  :root {
    --backdrop: #3a3a3a;
    --card-front: #e8e8e8;
    --card-back: #a7a7a7;
    --gold: #efcf72;
    --gold-soft: #f4de90;
    --text-grey: #8a8a8a;
  }
  * { margin: 0; padding: 0; box-sizing: border-box; }
  html, body {
    width: 1200px;
    height: 516px;
    overflow: hidden;
    background: var(--backdrop);
    font-family: "Questrial", "Century Gothic", sans-serif;
  }
  .stage {
    position: relative;
    width: 1200px;
    height: 516px;
  }
  .card {
    position: absolute;
    top: 134px;
    height: 245px;
    box-shadow: 0 4px 10px rgba(0,0,0,0.35);
  }
  .card--info {
    left: 141px;
    width: 439px;
    background: var(--card-front);
    color: var(--text-grey);
    text-align: center;
  }
  .card--brand {
    left: 606px;
    width: 454px;
    background: var(--card-back);
  }

  /* brand lockup: one colour, one weight */
  .brand {
    position: absolute;
    display: flex;
    align-items: center;
    gap: 12px;
    color: var(--gold);
    font-weight: 400;
  }
  .brand__dot {
    flex: none;
    border-radius: 50%;
    background: var(--gold);
  }
  .brand__name {
    display: flex;
    flex-direction: column;
    line-height: 1;
    text-transform: uppercase;
  }
  .brand__first { letter-spacing: 0.2em; }
  .brand__trade { letter-spacing: 0.08em; }

  .card--info .brand {
    left: 0;
    right: 0;
    top: 40px;
    justify-content: center;
  }
  .card--info .brand__dot { width: 30px; height: 30px; }
  .card--info .brand__first { font-size: 19px; }
  .card--info .brand__last { font-size: 19px; margin-top: 2px; }
  .card--info .brand__trade { font-size: 10px; margin-top: 4px; }

  .card--brand .brand {
    left: 110px;
    top: 112px;
  }
  .card--brand .brand__dot { width: 56px; height: 56px; }
  .card--brand .brand__first { font-size: 30px; }
  .card--brand .brand__last { font-size: 30px; margin-top: 3px; }
  .card--brand .brand__trade { font-size: 15px; margin-top: 6px; }

  .practitioner {
    position: absolute;
    left: 0;
    right: 0;
    top: 151px;
    font-size: 11px;
    line-height: 13px;
  }
  .practitioner__name {
    color: var(--gold);
    font-size: 12px;
    letter-spacing: 0.04em;
    text-transform: uppercase;
  }
  .contact {
    position: absolute;
    left: 0;
    right: 0;
    top: 196px;
    font-size: 10.5px;
    line-height: 13px;
  }
  .contact__row span + span { margin-left: 20px; }
  .contact__label { color: var(--gold); }
</style>
</head>
<body>
<main class="stage">

  <section class="card card--info" aria-label="Business card, contact side">
    <div class="brand">
      <span class="brand__dot" aria-hidden="true"></span>
      <span class="brand__name">
        <span class="brand__first">Marla</span>
        <span class="brand__last">Quenby</span>
        <span class="brand__trade">Acupuncture</span>
      </span>
    </div>

    <div class="practitioner">
      <p class="practitioner__name">Dr Marla Quenby</p>
      <p>(TCM Acupuncture)</p>
      <p>Acupuncture for balancing body and mind</p>
    </div>

    <div class="contact">
      <p class="contact__row">
        <span><span class="contact__label">M:</span> 94726150</span>
        <span><span class="contact__label">P:</span> 0438219574</span>
        <span><span class="contact__label">E:</span> Marlatcm@quenbymail.com</span>
      </p>
      <p>Fernleaf Wellcraft 14 Corran Lane, Elsworth 3071.</p>
    </div>
  </section>

  <section class="card card--brand" aria-label="Business card, brand side">
    <div class="brand">
      <span class="brand__dot" aria-hidden="true"></span>
      <span class="brand__name">
        <span class="brand__first">Marla</span>
        <span class="brand__last">Quenby</span>
        <span class="brand__trade">Acupuncture</span>
      </span>
    </div>
  </section>

</main>
</body>
</html>
```